I'm an electrician and the name of my company is called Brisk 'N' Bright Electrical. I require a professional business card that speaks to my clients, I also need it to be innovative and modern. We do maintenance & service work for domestic and commercial premises.

Industry/Entity Type

Electrical

Contact Information for Business Card

Must have the name of my company Brisk 'N' Bright Electrical, my name Darren Kolovos and my contact details 0427 381 592 and company email address Brisknbrightelectrical@mailvane.com and/or website Brisknbrightelectrical.com.au

Logo Text

Brisk 'N' Bright Electrical (If possible)

Colors
33a6d7
0592cd
3176b5

```html
<!DOCTYPE html>
<html lang="en">
<head>
<meta charset="utf-8">
<title>Brisk 'N' Bright Electrical – Business Card</title>
<link rel="stylesheet" href="https://fonts.googleapis.com/css2?family=Open+Sans:wght@400;600&family=Titillium+Web:wght@400&display=swap">
<style>
  :root {
    --stage: #8c8c8c;
    --navy: #0a2658;
    --royal: #3176b5;
    --azure: #0592cd;
    --sky: #33a6d7;
    --cyan-line: #19c3f2;
    --ice: #cdeaf8;
    --white: #ffffff;
    --name-blue: #0b5c9e;
    --grey-text: #9a9a9a;
  }
  * { margin: 0; padding: 0; box-sizing: border-box; }
  html, body { width: 1200px; height: 1200px; overflow: hidden; }
  body { background: var(--stage); position: relative; font-family: "Open Sans", sans-serif; }

  .card { position: absolute; left: 257px; width: 707px; height: 424px; overflow: hidden; }
  .card-front { top: 142px; }
  .card-back { top: 629px; background: var(--white); }

  .front-bg, .back-art { position: absolute; inset: 0; width: 100%; height: 100%; }

  .brand-mark {
    position: absolute; left: 324px; top: 154px; width: 58px; height: 58px;
    border-radius: 50%; background: var(--white);
  }
  .brand-name {
    position: absolute; left: 0; right: 0; top: 218px; text-align: center;
    font-family: "Titillium Web", sans-serif; font-weight: 400;
    font-size: 31px; line-height: 1; color: var(--white); text-transform: uppercase;
    letter-spacing: -0.5px;
  }
  .brand-tagline {
    position: absolute; left: 0; right: 0; top: 256px; text-align: center;
    font-size: 11px; letter-spacing: 4.5px; color: var(--white);
  }

  .holder { position: absolute; left: 88px; top: 104px; }
  .holder-name { font-size: 36px; font-weight: 600; color: var(--name-blue); line-height: 1.1; letter-spacing: -0.3px; }
  .holder-role, .holder-phone { font-size: 20px; color: var(--grey-text); line-height: 1.15; }

  .contact-list { position: absolute; left: 420px; right: 18px; top: 245px; list-style: none; color: var(--white); font-size: 12.5px; line-height: 18px; }
  .contact-list li { display: flex; align-items: flex-start; margin-bottom: 10px; white-space: nowrap; }
  .contact-list svg { width: 20px; height: 18px; flex: none; margin-right: 11px; }
</style>
</head>
<body>

<section class="card card-front">
  <svg class="front-bg" viewBox="0 0 707 424" role="img" aria-label="Deep blue background with a glowing centre and circuit-board trace pattern">
    <defs>
      <radialGradient id="frontGlow" cx="0.5" cy="0.45" r="0.75">
        <stop offset="0" stop-color="#0a86cc"/>
        <stop offset="0.45" stop-color="#0459a3"/>
        <stop offset="1" stop-color="#0a2658"/>
      </radialGradient>
    </defs>
    <rect width="707" height="424" fill="url(#frontGlow)"/>
  </svg>
  <div class="brand-mark"></div>
  <h1 class="brand-name">Brisk 'N' Bright Electrical</h1>
  <p class="brand-tagline">Domestic &amp; Commercial Service</p>
</section>

<section class="card card-back">
  <svg class="back-art" viewBox="0 0 707 424">
    <defs>
      <linearGradient id="topWash" x1="0" y1="0" x2="1" y2="0.6">
        <stop offset="0.35" stop-color="#ffffff"/>
        <stop offset="1" stop-color="#b9e3f7"/>
      </linearGradient>
      <linearGradient id="bandFill" x1="0" y1="0" x2="0" y2="1">
        <stop offset="0" stop-color="#0582c8"/>
        <stop offset="0.5" stop-color="#0457a0"/>
        <stop offset="1" stop-color="#0a2658"/>
      </linearGradient>
      <linearGradient id="edgeLine" x1="0" y1="0" x2="1" y2="0">
        <stop offset="0" stop-color="#cdeaf8"/>
        <stop offset="0.5" stop-color="#19c3f2"/>
        <stop offset="1" stop-color="#19c3f2"/>
      </linearGradient>
    </defs>
    <rect width="707" height="424" fill="url(#topWash)" role="img" aria-label="Light blue wash with faint circuit-board traces"/>
    <polygon points="0,234 305,234 346,197 707,197 707,424 0,424" fill="url(#edgeLine)"/>
    <polygon points="0,239 308,239 349,202 707,202 707,424 0,424" fill="url(#bandFill)" role="img" aria-label="Blue band with circuit-board trace pattern"/>
  </svg>

  <div class="holder">
    <h2 class="holder-name">Darren Kolovos</h2>
    <p class="holder-role">Director</p>
    <p class="holder-phone">0427 381 592</p>
  </div>

  <ul class="contact-list">
    <li>
      <svg viewBox="0 0 20 19"><path d="M10 1a6 6 0 0 0-6 6c0 4.5 6 11 6 11s6-6.5 6-11a6 6 0 0 0-6-6z" fill="#fff"/><circle cx="10" cy="7" r="2.3" fill="#0582c8"/></svg>
      <span>27 Quillon Lane,<br>Ostvale Park 9081</span>
    </li>
    <li>
      <svg viewBox="0 0 20 19"><rect x="5.5" y="1" width="9" height="17" rx="1.2" fill="none" stroke="#fff" stroke-width="1.8"/><circle cx="10" cy="15" r="1" fill="#fff"/></svg>
      <span>0427 381 592</span>
    </li>
    <li>
      <svg viewBox="0 0 20 19"><path d="M4 1h8l4 4v13H4z" fill="none" stroke="#fff" stroke-width="1.6"/><path d="M7 10h6M7 13.5h6" stroke="#fff" stroke-width="1.5"/></svg>
      <span>Brisknbrightelectrical.com.au</span>
    </li>
    <li>
      <svg viewBox="0 0 20 19"><rect x="1" y="4" width="18" height="12" rx="1" fill="#fff"/><path d="M1.5 4.5l8.5 6.5 8.5-6.5" fill="none" stroke="#0457a0" stroke-width="1.5"/></svg>
      <span>Brisknbrightelectrical@mailvane.com</span>
    </li>
  </ul>
</section>

</body>
</html>
```